Tooth Fairy Certificates with a Brown Tooth Fairy character on it (animation)
Tooth Certificate
I needs a name and date slot
also boxes for checks or stars next to each word
- clean
- shiny
- needs more brushing

Great Job, I'm so Proud of you! keep up the great brushing!

I need 4 per 11x8 page or 2- 5' 7 per page.

```html
<!DOCTYPE html>
<html lang="en">
<head>
<meta charset="utf-8">
<title>Tooth Fairy Certificate</title>
<link rel="stylesheet" href="https://fonts.googleapis.com/css2?family=Oswald:wght@300;400;600&family=Pinyon+Script&family=Patrick+Hand&display=swap">
<style>
  :root {
    --page-pink: #f8c6d2;
    --frame-pink: #ef7fa0;
    --card-cream: #fdfbef;
    --title-brown: #cf7a2a;
    --accent-gold: #f2b93b;
    --script-gold: #d89a45;
    --message-brown: #c98a2a;
    --icon-tint: #f6e3c8;
    --fairy-rose: #f7a58f;
    --fairy-lilac: #e6d3f2;
    --tooth-blue: #e4f2f8;
    --tooth-pink: #f6b8c8;
  }
  * { margin: 0; padding: 0; box-sizing: border-box; }
  html, body { width: 1200px; height: 848px; overflow: hidden; background: var(--page-pink); }
  .certificate { position: relative; width: 1200px; height: 848px; background: var(--page-pink); }
  .card {
    position: absolute; left: 120px; top: 87px; width: 973px; height: 673px;
    background: var(--card-cream); border: 6px solid var(--frame-pink); border-radius: 14px;
  }
  .fairy-art {
    position: absolute; left: 13px; top: 0; width: 347px; height: 533px;
    background: linear-gradient(160deg, var(--fairy-rose) 0%, var(--fairy-lilac) 60%, #f6dfe8 100%);
    border-radius: 40% 40% 30% 30%; opacity: .9;
  }
  .mascot-art {
    position: absolute; left: 960px; top: 573px; width: 240px; height: 275px;
    background: linear-gradient(180deg, var(--tooth-blue) 0%, var(--tooth-blue) 60%, var(--tooth-pink) 100%);
    border-radius: 45% 45% 20% 20%;
  }
  .title {
    position: absolute; left: 0; width: 1200px; text-align: center;
    font-family: "Oswald", sans-serif; font-weight: 600; font-size: 62px;
    color: var(--title-brown); line-height: 1; letter-spacing: 1px;
  }
  .title--top { top: 118px; }
  .title--bottom { top: 200px; }
  .divider { position: absolute; left: 460px; top: 280px; width: 300px; border-top: 3px dashed var(--frame-pink); }
  .awarded {
    position: absolute; left: 0; width: 1200px; top: 310px; text-align: center;
    font-family: "Oswald", sans-serif; font-weight: 400; font-size: 27px; color: var(--accent-gold);
  }
  .recipient {
    position: absolute; left: 0; width: 1200px; top: 345px; text-align: center;
    font-family: "Pinyon Script", cursive; font-size: 64px; color: var(--script-gold); line-height: 1.2;
  }
  .rating { position: absolute; width: 110px; text-align: center; top: 448px; }
  .rating--clean { left: 372px; }
  .rating--shiny { left: 518px; }
  .rating--brush { left: 672px; }
  .rating__icon {
    width: 72px; height: 80px; margin: 0 auto; border-radius: 30px 30px 18px 18px;
    background: var(--icon-tint); border: 2px solid var(--title-brown);
  }
  .rating__label {
    margin-top: 8px; font-family: "Oswald", sans-serif; font-weight: 400;
    font-size: 14px; line-height: 1.5; color: var(--accent-gold);
  }
  .message {
    position: absolute; left: 0; width: 1200px; top: 580px; text-align: center;
    font-family: "Patrick Hand", cursive; font-size: 25px; color: var(--message-brown); letter-spacing: .5px;
  }
  .date {
    position: absolute; left: 760px; width: 180px; top: 646px; text-align: right;
    font-family: "Oswald", sans-serif; font-weight: 300; font-size: 27px; color: var(--accent-gold);
  }
  .signoff {
    position: absolute; left: 0; width: 1160px; text-align: center;
    font-family: "Patrick Hand", cursive; font-size: 24px; color: var(--message-brown);
  }
  .signoff--greeting { top: 674px; }
  .signoff--name { top: 712px; }
</style>
</head>
<body>
<main class="certificate">
  <section class="card"></section>
  <div class="fairy-art" role="img" aria-label="Illustration of a smiling tooth fairy with wings and a pink tutu"></div>
  <div class="mascot-art" role="img" aria-label="Illustration of a cartoon tooth with a crown and wand"></div>

  <h1 class="title title--top">TOOTH FAIRY</h1>
  <h1 class="title title--bottom">CERTIFICATE</h1>
  <div class="divider"></div>

  <p class="awarded">awarded to</p>
  <p class="recipient">Nora Bell</p>

  <div class="rating rating--clean">
    <div class="rating__icon" role="img" aria-label="Tooth icon for clean"></div>
    <p class="rating__label">Clean</p>
  </div>
  <div class="rating rating--shiny">
    <div class="rating__icon" role="img" aria-label="Sparkling tooth icon for shiny"></div>
    <p class="rating__label">Shiny</p>
  </div>
  <div class="rating rating--brush">
    <div class="rating__icon" role="img" aria-label="Tooth with toothbrush icon"></div>
    <p class="rating__label">Needs<br>more brushing</p>
  </div>

  <p class="message">Great Job, I'm so Proud of you! keep up the great brushing!</p>
  <p class="date">23 May, 2022</p>
  <p class="signoff signoff--greeting">With love,</p>
  <p class="signoff signoff--name">The Tooth Fairy</p>
</main>
</body>
</html>
```